10 Labels for Wild Bird Food

Label Design Request for New Products
We are excited to announce the launch of 10 new products and are seeking vibrant, fun, and colorful labels to match their energy. Each label should measure 6 x 4 inches (152.4mm x 101.6mm) and must feature our brand logo. Additionally, please include all the necessary information as detailed in the attached Word document.

Let's make our products stand out on the shelves with eye-catching designs!

Target Market(s)

Wild Bird Food Buyers

Requirements
Must have
• Logo

```html
<!DOCTYPE html>
<html lang="en">
<head>
<meta charset="utf-8">
<title>Perch Pantry – Wild Bird Food Labels</title>
<link href="https://fonts.googleapis.com/css2?family=Baloo+2:wght@700;800&family=Open+Sans:wght@400;700&display=swap" rel="stylesheet">
<style>
:root{
  --orange:#f7890f; --sun:#fbba0b; --teal:#168a80; --leaf:#8dbb22;
  --olive:#b3951a; --brown:#8b6418; --mustard:#ebc232; --wheat:#c9a02d;
  --purple:#8e1b7d; --pink:#e6008a; --sky:#00a9e6; --white:#fff;
}
*{box-sizing:border-box;margin:0;padding:0}
html,body{width:857px;height:1200px;overflow:hidden;background:var(--white)}
body{position:relative;font-family:"Open Sans",sans-serif;color:var(--white)}
.sheet{position:absolute;inset:0}
.label{position:absolute;width:230px;height:345px;border-radius:22px;overflow:hidden;background:var(--body)}
.col-1{left:40px}.col-2{left:313px}.col-3{left:592px}
.row-1{top:47px}.row-2{top:430px}.row-3{top:815px}

.label__brand{position:absolute;left:0;top:0;width:100%;height:80px;background:var(--head);display:flex;align-items:center;padding-left:38px;gap:10px}
.brand__mark{width:30px;height:30px;border-radius:50%;background:var(--white);flex:none}
.brand__name{font-family:"Baloo 2",sans-serif;font-weight:700;font-size:26px;line-height:.82;color:var(--white)}

.label__title{position:absolute;left:0;top:80px;width:100%;height:74px;background:var(--band);display:flex;align-items:center;justify-content:center;text-align:center;font-family:"Baloo 2",sans-serif;font-weight:800;font-size:41px;line-height:.8;letter-spacing:-.5px;padding-top:7px;white-space:nowrap}
.label__title--wide{font-size:36px;letter-spacing:-.8px}

.label__art{position:absolute;left:86px;top:160px;width:144px;height:180px;background:var(--bird);border-radius:48% 30% 45% 60% / 40% 35% 65% 55%;opacity:.85}
.label__perch{position:absolute;left:42px;top:262px;width:142px;height:7px;border-radius:4px;background:var(--bird)}

.label__pitch{position:absolute;left:8px;top:159px;width:96px;text-align:center}
.pitch__head{font-family:"Baloo 2",sans-serif;font-weight:700;font-size:9px;line-height:.95;margin-bottom:3px}
.pitch__copy{font-size:4.4px;line-height:1.35}

.label__use{position:absolute;left:122px;top:180px;width:100px;text-align:center}
.use__head{font-family:"Baloo 2",sans-serif;font-weight:700;font-size:9.5px;line-height:1;margin-bottom:3px}
.use__copy{font-size:5px;line-height:1.45}

.label__weight{position:absolute;left:0;top:274px;width:100%;text-align:center;font-family:"Baloo 2",sans-serif;font-weight:700;font-size:9.5px}
.label__sku{position:absolute;left:20px;top:288px;font-size:5px;font-weight:700}

.label__codes{position:absolute;left:100px;top:297px;width:42px;font-size:4.5px;font-weight:700}
.codes__box{display:block;height:10px;background:var(--white);border-radius:1px;margin:1px 0 7px}

.label__contact{position:absolute;left:146px;top:293px;width:80px;font-size:4.5px;font-weight:700;line-height:1.5;font-style:normal}
</style>
</head>
<body>
<main class="sheet">

<article class="label col-1 row-1" style="--head:var(--orange);--band:var(--sun);--body:var(--orange);--bird:var(--sun)">
  <header class="label__brand"><span class="brand__mark"></span><span class="brand__name">Perch<br>Pantry</span></header>
  <h2 class="label__title">Sunflower<br>Hearts</h2>
  <div class="label__art" role="img" aria-label="Illustration of a songbird perched on a branch"></div>
  <div class="label__perch"></div>
  <section class="label__pitch"><h3 class="pitch__head">Enhance Your Garden with the Best Bird Feed!</h3><p class="pitch__copy">Transform your garden into a bird haven with our Sunflower Hearts 5L Bag, the ultimate bird food for attracting a wide variety of beautiful feathered friends. Packed with essential nutrients and energy, these premium sunflower hearts are a must-have for any bird enthusiast.</p></section>
  <section class="label__use"><h3 class="use__head">Easy to Use:</h3><p class="use__copy">Simply fill your bird feeders, sprinkle on bird tables, or scatter on the ground to attract a delightful array of garden birds. Watch as they flock to your garden, bringing life, color, and joy to your outdoor space.</p></section>
  <p class="label__weight">5L - Net Weight: 2900g</p>
  <p class="label__sku">SKU: PP21</p>
  <div class="label__codes">Batch:<span class="codes__box"></span>Expiry Date:<span class="codes__box"></span></div>
  <address class="label__contact">Address: Marlow Imports, Brookside Trade Park, Ashford, AB12 3CD<br>sales@marlowimports.example<br>Not for human consumption<br>May Contain Nuts</address>
</article>

<article class="label col-2 row-1" style="--head:var(--teal);--band:var(--leaf);--body:var(--teal);--bird:var(--leaf)">
  <header class="label__brand"><span class="brand__mark"></span><span class="brand__name">Perch<br>Pantry</span></header>
  <h2 class="label__title">Peanuts</h2>
  <div class="label__art" role="img" aria-label="Illustration of a songbird perched on a branch"></div>
  <div class="label__perch"></div>
  <section class="label__pitch"><h3 class="pitch__head">Delight Your Garden Birds with Nutritious Peanuts!</h3><p class="pitch__copy">Attract a vibrant variety of feathered friends to your garden with our Peanuts 5L Bag, the perfect choice for bird enthusiasts who want to provide their avian visitors with a high-energy, nutritious treat. Packed with essential nutrients, our premium peanuts are a favorite among many bird species, ensuring your garden becomes a lively and colorful sanctuary.</p></section>
  <section class="label__use"><h3 class="use__head">Easy to Use:</h3><p class="use__copy">Fill your bird feeders, place on bird tables, or scatter on the ground to create an inviting space for birds. Watch as they flock to your garden, adding beauty and song to your outdoor area.</p></section>
  <p class="label__weight">5L - Net Weight: 3100g</p>
  <p class="label__sku">SKU: PP22</p>
  <div class="label__codes">Batch:<span class="codes__box"></span>Expiry Date:<span class="codes__box"></span></div>
  <address class="label__contact">Address: Marlow Imports, Brookside Trade Park, Ashford, AB12 3CD<br>sales@marlowimports.example<br>Not for human consumption<br>May Contain Nuts</address>
</article>

<article class="label col-3 row-1" style="--head:var(--olive);--band:var(--sun);--body:var(--olive);--bird:var(--sun)">
  <header class="label__brand"><span class="brand__mark"></span><span class="brand__name">Perch<br>Pantry</span></header>
  <h2 class="label__title label__title--wide">Dried<br>Mealworms</h2>
  <div class="label__art" role="img" aria-label="Illustration of a songbird perched on a branch"></div>
  <div class="label__perch"></div>
  <section class="label__pitch"><h3 class="pitch__head">Elevate Your Bird Feeding Experience with Nutritious Mealworms!</h3><p class="pitch__copy">Create a thriving bird haven in your garden with our Dried Mealworms 5L Bag, the ultimate protein-rich treat for your feathered friends. Ideal for attracting a wide range of bird species, these premium dried mealworms are packed with essential nutrients, ensuring your garden birds stay healthy and energetic.</p></section>
  <section class="label__use"><h3 class="use__head">Easy to Use:</h3><p class="use__copy">Add to your bird feeders, sprinkle on bird tables, or mix with other bird food to create an irresistible feast for your garden birds. Watch as they flock to your garden, bringing vibrant colors and joyful chirping to your outdoor space</p></section>
  <p class="label__weight">5L - Net Weight: 800g</p>
  <p class="label__sku">SKU: PP23</p>
  <div class="label__codes">Batch:<span class="codes__box"></span>Expiry Date:<span class="codes__box"></span></div>
  <address class="label__contact">Address: Marlow Imports, Brookside Trade Park, Ashford, AB12 3CD<br>sales@marlowimports.example<br>Not for human consumption<br>May Contain Nuts</address>
</article>

<article class="label col-1 row-2" style="--head:var(--brown);--band:var(--mustard);--body:var(--brown);--bird:var(--wheat)">
  <header class="label__brand"><span class="brand__mark"></span><span class="brand__name">Perch<br>Pantry</span></header>
  <h2 class="label__title">Calci<br>Worms</h2>
  <div class="label__art" role="img" aria-label="Illustration of a songbird perched on a branch"></div>
  <div class="label__perch"></div>
  <section class="label__pitch"><h3 class="pitch__head">Boost Your Garden Birds' Health with Nutritious Calci Worms!</h3><p class="pitch__copy">Attract a vibrant array of feathered friends to your garden with our Calci Worms 5L Bag, the ultimate calcium-rich treat for your avian visitors. Perfect for bird enthusiasts, these premium calci worms are packed with essential nutrients, ensuring your garden birds stay healthy, strong, and energetic.</p></section>
  <section class="label__use"><h3 class="use__head">Easy to Use:</h3><p class="use__copy">Add to your bird feeders, sprinkle on bird tables, or mix with other bird food to create an irresistible feast for your garden birds. Watch as they flock to your garden, bringing vibrant colors and joyful chirping to your outdoor space</p></section>
  <p class="label__weight">5L - Net Weight: 800g</p>
  <p class="label__sku">SKU: PP24</p>
  <div class="label__codes">Batch:<span class="codes__box"></span>Expiry Date:<span class="codes__box"></span></div>
  <address class="label__contact">Address: Marlow Imports, Brookside Trade Park, Ashford, AB12 3CD<br>sales@marlowimports.example<br>Not for human consumption<br>May Contain Nuts</address>
</article>

<article class="label col-2 row-2" style="--head:var(--teal);--band:var(--sun);--body:var(--teal);--bird:var(--sun)">
  <header class="label__brand"><span class="brand__mark"></span><span class="brand__name">Perch<br>Pantry</span></header>
  <h2 class="label__title">Peanuts<br>In Shell</h2>
  <div class="label__art" role="img" aria-label="Illustration of a songbird perched on a branch"></div>
  <div class="label__perch"></div>
  <section class="label__pitch"><h3 class="pitch__head">Delight Your Garden Birds with Nutritious, Fun-to-Crack Peanuts!</h3><p class="pitch__copy">Transform your garden into a lively bird sanctuary with our Peanuts in Shell 5L Bag, the perfect choice for bird enthusiasts who want to provide their avian visitors with a delicious and engaging treat. Packed with essential nutrients, our premium in-shell peanuts are a favorite among many bird species.</p></section>
  <section class="label__use"><h3 class="use__head">Easy to Use:</h3><p class="use__copy">Fill your bird feeders, place on bird tables, or scatter on the ground to create an inviting space for birds. Watch as they flock to your garden, adding beauty and song to your outdoor area</p></section>
  <p class="label__weight">5L - Net Weight: 1300g</p>
  <p class="label__sku">SKU: PP25</p>
  <div class="label__codes">Batch:<span class="codes__box"></span>Expiry Date:<span class="codes__box"></span></div>
  <address class="label__contact">Address: Marlow Imports, Brookside Trade Park, Ashford, AB12 3CD<br>sales@marlowimports.example<br>Not for human consumption<br>May Contain Nuts</address>
</article>

<article class="label col-3 row-2" style="--head:var(--purple);--band:var(--sun);--body:var(--purple);--bird:var(--sun)">
  <header class="label__brand"><span class="brand__mark"></span><span class="brand__name">Perch<br>Pantry</span></header>
  <h2 class="label__title label__title--wide">Niger Seed</h2>
  <div class="label__art" role="img" aria-label="Illustration of a songbird perched on a branch"></div>
  <div class="label__perch"></div>
  <section class="label__pitch"><h3 class="pitch__head">Attract a Burst of Color to Your Garden with Nutritious Niger Seed!</h3><p class="pitch__copy">Invite a beautiful array of small, colorful birds to your garden with our Niger Seed 5L Bag, the top choice for bird enthusiasts who want to provide a nutrient-rich and highly desirable treat. Known for its appeal to finches and other small birds, this seed makes your garden a vibrant bird haven.</p></section>
  <section class="label__use"><h3 class="use__head">Easy to Use:</h3><p class="use__copy">Fill your niger seed feeders or sprinkle on bird tables to create an irresistible feast for your garden birds. Watch as they flock to your garden, bringing vibrant colors and cheerful chirping to your outdoor space.</p></section>
  <p class="label__weight">5L - Net Weight: 3300g</p>
  <p class="label__sku">SKU: PP26</p>
  <div class="label__codes">Batch:<span class="codes__box"></span>Expiry Date:<span class="codes__box"></span></div>
  <address class="label__contact">Address: Marlow Imports, Brookside Trade Park, Ashford, AB12 3CD<br>sales@marlowimports.example<br>Not for human consumption<br>May Contain Nuts</address>
</article>

<article class="label col-1 row-3" style="--head:var(--purple);--band:var(--pink);--body:var(--purple);--bird:var(--pink)">
  <header class="label__brand"><span class="brand__mark"></span><span class="brand__name">Perch<br>Pantry</span></header>
  <h2 class="label__title">Wild Bird<br>Mix</h2>
  <div class="label__art" role="img" aria-label="Illustration of a songbird perched on a branch"></div>
  <div class="label__perch"></div>
  <section class="label__pitch"><h3 class="pitch__head">Transform Your Garden into a Bird Sanctuary with Our Nutritious Wild Bird Mix!</h3><p class="pitch__copy">Invite a diverse array of feathered friends to your garden with our Wild Bird Mix 5L Bag, the perfect choice for bird enthusiasts who want to give their avian visitors a balanced and tasty diet. Packed with high-quality seeds and grains, this premium food nourishes a wide range of species.</p></section>
  <section class="label__use"><h3 class="use__head">Easy to Use:</h3><p class="use__copy">Fill your bird feeders, place on bird tables, or scatter on the ground to create an inviting space for birds. Watch as they flock to your garden, adding beauty and joyful song to your outdoor area.</p></section>
  <p class="label__weight">5L - Net Weight: 3300g</p>
  <p class="label__sku">SKU: PP27</p>
  <div class="label__codes">Batch:<span class="codes__box"></span>Expiry Date:<span class="codes__box"></span></div>
  <address class="label__contact">Address: Marlow Imports, Brookside Trade Park, Ashford, AB12 3CD<br>sales@marlowimports.example<br>Not for human consumption<br>May Contain Nuts</address>
</article>

<article class="label col-2 row-3" style="--head:var(--leaf);--band:var(--teal);--body:var(--leaf);--bird:var(--teal)">
  <header class="label__brand"><span class="brand__mark"></span><span class="brand__name">Perch<br>Pantry</span></header>
  <h2 class="label__title">No Mess<br>Mix</h2>
  <div class="label__art" role="img" aria-label="Illustration of a songbird perched on a branch"></div>
  <div class="label__perch"></div>
  <section class="label__pitch"><h3 class="pitch__head">Enjoy a Clean and Vibrant Garden with Our Nutritious No Mess Mix!</h3><p class="pitch__copy">Invite a diverse array of beautiful birds to your garden without the hassle of leftover shells and debris with our No Mess Mix 5L Bag. This premium bird food is a nutritious, easy-to-eat blend that leaves no waste, ensuring your garden remains clean and your feathered visitors are well-fed.</p></section>
  <section class="label__use"><h3 class="use__head">Easy to Use:</h3><p class="use__copy">Fill your bird feeders, place on bird tables, or scatter on the ground to create an inviting and clean feeding space for birds. Watch as they flock to your garden, bringing vibrant colors and joyful chirping to your outdoor area.</p></section>
  <p class="label__weight">5L - Net Weight: 3200g</p>
  <p class="label__sku">SKU: PP28</p>
  <div class="label__codes">Batch:<span class="codes__box"></span>Expiry Date:<span class="codes__box"></span></div>
  <address class="label__contact">Address: Marlow Imports, Brookside Trade Park, Ashford, AB12 3CD<br>sales@marlowimports.example<br>Not for human consumption<br>May Contain Nuts</address>
</article>

<article class="label col-3 row-3" style="--head:var(--teal);--band:var(--sky);--body:var(--teal);--bird:var(--sky)">
  <header class="label__brand"><span class="brand__mark"></span><span class="brand__name">Perch<br>Pantry</span></header>
  <h2 class="label__title">Peanut<br>Granules</h2>
  <div class="label__art" role="img" aria-label="Illustration of a songbird perched on a branch"></div>
  <div class="label__perch"></div>
  <section class="label__pitch"><h3 class="pitch__head">Nourish Your Garden Birds with Delicious, Nutritious Peanut Granules!</h3><p class="pitch__copy">Transform your garden into a vibrant bird sanctuary with our Peanut Granules 5L Bag, the perfect choice for bird enthusiasts who want to give their avian visitors a high-energy, nutrient-rich treat. Ideal for a wide variety of species, these granules make your garden a favorite feeding spot.</p></section>
  <section class="label__use"><h3 class="use__head">Easy to Use:</h3><p class="use__copy">Fill your bird feeders, sprinkle on bird tables, or mix with other bird food to create an irresistible feast for your garden birds. Watch as they flock to your garden, bringing vibrant colors and joyful chirping to your outdoor space.</p></section>
  <p class="label__weight">5L - Net Weight: 2800g</p>
  <p class="label__sku">SKU: PP29</p>
  <div class="label__codes">Batch:<span class="codes__box"></span>Expiry Date:<span class="codes__box"></span></div>
  <address class="label__contact">Address: Marlow Imports, Brookside Trade Park, Ashford, AB12 3CD<br>sales@marlowimports.example<br>Not for human consumption<br>May Contain Nuts</address>
</article>

</main>
</body>
</html>
```